Web Design Project

We need web design for a new baby products (nursery furniture) business in Australia.

The logo is already done, and I would like to reflect a similar theme throughout the website:
* Clean, white background.
* Use of lime green, purple and orange.
* Similar font to logo for headings
* FUNKY, FASHIONABLE, QUALITY feeling of website.

The main concept is to be attractive to discerning mums who are buying big items like a cot or chest of drawers. These are expensive items and will be considered the most important purchases for a newborn, so the website has to be enticing!!!
Updates

Hello,

Thank you for your submissions. I have received a few questions regarding the font and the coding of this website.

The job I am seeking is for design for an E-commerce store. The font was done by another craft hive designer, so I do not know what type of font I am sorry.

I was hoping to have more designs by now, so please send them soon, this project is guaranteed!

I also ask you to read the brief properly please. The name of the business is Cradle Lane, as the logo says. The use of design that I have mentioned has only been demonstrated in a couple of designs submitted to me.

I look forward to seeing your work soon!

Kind Regards
Marla

Target Market(s)

Young mothers aged 25-45

Industry/Entity Type

Business

Requirements
Must have
• Must be funky, bright, energetic, attractive visually.
Nice to have
• I like the idea of some floral / design work in faded lime green, purple on some of the edges of different pages. Maybe islamic design? But has to be very fashionable.
Should not have
• Should not have any traditional ideas of baby websites.

ie- no stork, nappy images, teddybears etc.

```html
<!DOCTYPE html>
<html lang="en">
<head>
<meta charset="utf-8">
<title>Cradle Lane – Nursery Furniture</title>
<link rel="stylesheet" href="https://fonts.googleapis.com/css2?family=Nunito:wght@700;800&family=Source+Sans+3:wght@400;600&display=swap">
<style>
:root{
  --lime-bg:#e3eb9a;
  --white:#ffffff;
  --purple:#7b22b4;
  --purple-light:#a24ee0;
  --purple-text:#6a1fa3;
  --green:#6b9a1c;
  --green-dark:#557d12;
  --orange:#e5890a;
  --orange-text:#d47a10;
  --text:#444444;
  --muted:#8a8a8a;
  --panel:#f1f1f1;
  --footer:#5e5e5e;
  --body-font:"Source Sans 3",sans-serif;
  --head-font:"Nunito",sans-serif;
}
*{box-sizing:border-box;margin:0;padding:0}
html,body{width:952px;height:1200px;overflow:hidden}
body{position:relative;font-family:var(--body-font);color:var(--text);background:var(--lime-bg)}
.backdrop{position:absolute;inset:0;background:linear-gradient(90deg,#dfe78f,#ecf1b4 50%,#dfe78f)}
.page{position:absolute;left:70px;top:8px;width:813px;height:1178px;background:var(--white);box-shadow:0 0 6px rgba(0,0,0,.15)}
.abs{position:absolute}

/* header */
.brand{left:9px;top:20px;display:flex;align-items:center;gap:8px}
.brand-dot{width:46px;height:46px;border-radius:50%;background:var(--green)}
.brand-name{font-family:var(--head-font);font-weight:800;font-size:30px;line-height:1;color:var(--purple-light)}
.account-links{left:350px;top:35px;display:flex;font-size:11px;color:#555}
.account-links span{padding:0 9px}
.account-links span+span{border-left:1px solid #777}
.search{left:693px;top:25px;width:106px;height:20px;border:1px solid #ccc;border-radius:2px;font-size:9px;font-style:italic;color:#aaa;padding:4px 6px;display:flex;justify-content:space-between;align-items:center}
.header-rule{left:215px;top:65px;width:590px;height:10px;background:#ececec}

/* nav */
.main-nav{left:9px;top:91px;width:796px;height:38px;background:linear-gradient(#a343e2,#7b22b4);display:flex;border:1px solid #6a1a9f}
.main-nav a{color:#fff;text-decoration:none;font-size:11.5px;display:flex;align-items:center;justify-content:center;border-right:1px solid #9a4ad2;flex:auto}
.main-nav a:last-child{border-right:none}
.main-nav a.current{background:#b25fe8}

/* hero */
.hero{left:7px;top:135px;width:798px;height:267px;background:#eeeeee;padding:6px}
.hero-inner{position:relative;width:100%;height:100%;background:linear-gradient(90deg,#eef1ee,#d3e0da 55%,#c9d8d2);overflow:hidden}
.hero-photo{position:absolute;right:0;top:0;width:365px;height:100%;background:linear-gradient(135deg,#d8e1dc,#b9c7c6 50%,#e7e9e6)}
.hero-title{position:absolute;left:43px;top:38px;font-size:27px;line-height:35px;font-weight:400;color:#555}
.hero-title .light{color:#888}
.hero-btn{position:absolute;left:43px;top:121px;width:80px;height:28px;background:#fff;border:1px solid #ddd;border-radius:3px;font-size:12px;color:#666;display:flex;align-items:center;justify-content:center}
.hero-dots{position:absolute;left:148px;top:188px;display:flex;gap:11px}
.hero-dots i{width:9px;height:9px;border-radius:50%;background:#fff}
.hero-dots i.on{background:#555}

/* welcome */
.welcome{left:9px;top:430px;width:796px}
.welcome h1{font-weight:400;font-size:21px;color:#444}
.welcome h1 b{font-weight:400;color:var(--purple-text)}
.welcome p{margin-top:12px;font-size:10.3px;line-height:18.3px;text-align:justify;color:#555}
.rule{left:9px;width:796px;height:1px;background:#e6e6e6}

/* products */
.section-title{font-size:17px;color:var(--purple-text);font-weight:400}
.recent{left:9px;top:553px;width:558px}
.dotted{margin-top:9px;border-top:1px dotted #888}
.product-grid{display:grid;grid-template-columns:repeat(4,118px);column-gap:29px;row-gap:18px;margin-top:13px;margin-left:2px}
.product{text-align:center}
.product-name{font-size:10.5px;color:#444;height:15px}
.product-img{height:88px;border:3px solid #eee;border-radius:3px}
.img-a{background:linear-gradient(135deg,#e8d6a8,#a9743c)}
.img-b{background:linear-gradient(135deg,#c9c5bf,#f4f4f4 60%,#c84a3e)}
.img-c{background:radial-gradient(circle,#4a3a30,#f2f2f2 70%)}
.img-d{background:linear-gradient(90deg,#e9ddc2,#5c4536 50%,#e9e4d6)}
.price{font-family:var(--head-font);font-weight:800;color:var(--orange);font-size:15px;text-align:left;padding-left:21px;margin-top:3px;height:20px}
.product-actions{display:flex;height:23px;border-radius:3px;background:linear-gradient(#7fae2c,var(--green-dark));color:#fff;font-size:9.5px}
.product-actions span{flex:1;display:flex;align-items:center;justify-content:center}
.product-actions span+span{border-left:1px solid #8fbd42}

/* sidebar */
.newsletter{left:578px;top:557px;width:227px;height:110px;background:var(--green);border-radius:3px;padding:9px 10px}
.newsletter h3{color:#fff;font-weight:400;font-size:13px}
.newsletter .dotted{border-top-color:#c2dc8a;margin:8px -10px 0}
.newsletter .email{margin:12px 0 0 3px;height:25px;border-radius:13px;background:#fff;font-size:10px;font-style:italic;color:#aaa;padding:6px 15px}
.newsletter .submit{margin:7px 0 0 auto;width:58px;height:19px;border-radius:10px;background:linear-gradient(#ffbd2e,var(--orange));color:#fff;font-size:9px;font-weight:600;display:flex;align-items:center;justify-content:center}
.promo{left:583px;top:680px;width:217px;height:262px;background:linear-gradient(#fff,#ececec);border:1px solid #e3e3e3}
.promo-img{position:absolute;left:12px;top:15px;width:118px;height:100px;background:linear-gradient(135deg,#6a4a34,#f5f5f5 55%,#8a6a4e)}
.promo-badge{position:absolute;left:145px;top:22px;width:55px;height:55px;border-radius:50%;background:var(--orange)}
.promo h3{position:absolute;left:16px;top:128px;font-weight:400;font-size:16.5px;color:#b05f0c}
.promo p{position:absolute;left:18px;top:157px;width:188px;font-size:10px;line-height:16.5px;color:#555;text-align:justify}
.promo-cart{position:absolute;left:16px;top:218px;width:93px;height:24px;border-radius:12px;background:linear-gradient(#c17a30,#8c4f16);color:#fff;font-size:11px;display:flex;align-items:center;justify-content:center;gap:5px}
.promo-more{position:absolute;left:117px;top:218px;width:84px;height:24px;border-radius:12px;background:linear-gradient(#a6a6a6,#7a7a7a);color:#fff;font-size:11px;display:flex;align-items:center;justify-content:center;gap:5px}

/* testimonials */
.testimonials-title{left:0;top:982px;width:813px;text-align:center;font-size:15px;color:var(--orange-text)}
.testimonial{left:7px;top:1011px;width:798px;height:81px;background:var(--panel);border-radius:6px}
.quote-mark{position:absolute;font-family:Georgia,serif;font-size:46px;color:#d0d0d0;line-height:1}
.testimonial p{position:absolute;left:60px;top:16px;width:705px;font-size:10px;line-height:16.5px;color:#555}
.testimonial cite{position:absolute;right:66px;top:58px;font-style:normal;font-size:10px;color:var(--purple-text)}

/* footer */
.site-footer{left:7px;top:1100px;width:798px;height:75px;background:linear-gradient(#6a6a6a,#4f4f4f);color:#fff}
.footer-links{position:absolute;left:24px;top:12px;display:flex;font-size:9.5px}
.footer-links span{padding:0 7px}
.footer-links span:first-child{padding-left:0}
.footer-links span+span{border-left:1px solid #ccc}
.copyright{position:absolute;left:24px;top:51px;font-size:9.5px}
.social{position:absolute;right:24px;top:47px;display:flex;gap:6px}
.social i{width:17px;height:17px;border-radius:50%;background:#fff}
</style>
</head>
<body>
<div class="backdrop" role="img" aria-label="Faded lime and purple floral pattern border"></div>

<div class="page">
  <header>
    <div class="abs brand"><span class="brand-dot"></span><span class="brand-name">Cradle Lane</span></div>
    <nav class="abs account-links"><span>My Cart</span><span>My Account</span><span>Check out</span><span>Log in</span><span>Register</span></nav>
    <div class="abs search">Search
      <svg width="8" height="8" viewBox="0 0 10 10"><circle cx="4" cy="4" r="3" fill="none" stroke="#aaa" stroke-width="1.4"/><line x1="6.3" y1="6.3" x2="9.5" y2="9.5" stroke="#aaa" stroke-width="1.4"/></svg>
    </div>
    <div class="abs header-rule"></div>
    <nav class="abs main-nav">
      <a class="current" href="#">HOME</a><a href="#">ABOUT US</a><a href="#">OUR PRODUCTS</a><a href="#">SHIPPING DETAILS</a><a href="#">CLIENT’S TESTIMONIALS</a><a href="#">SPECIAL OFFERS</a><a href="#">CONTACT US</a>
    </nav>
  </header>

  <section class="abs hero">
    <div class="hero-inner">
      <div class="hero-photo" role="img" aria-label="Mother holding her baby on a white nursery bench beside a cot"></div>
      <h2 class="hero-title"><span class="light">Perfect nursery furniture</span><br>for you Baby</h2>
      <div class="hero-btn">View more</div>
      <div class="hero-dots"><i></i><i class="on"></i><i></i><i></i></div>
    </div>
  </section>

  <section class="abs welcome">
    <h1>Welcome to <b>Little Nest</b></h1>
    <p>Sed ut perspiciatis unde omnis iste natus error sit voluptatem accusantium doloremque laudantium, totam rem aperiam, eaque ipsa quae ab illo inventore veritatis et quasi archi tecto beatae vitae dicta sunt explicabo. Nemo enim ipsam voluptatem quia voluptas sit aspernatur aut odit aut fugit, sed quia consequuntur magni dolores eos qui ratione voluptatem sequi nesciunt. Neque porro quisquam est, qui dolorem ipsum quia dolor sit amet, consectetur.</p>
  </section>
  <div class="abs rule" style="top:536px"></div>

  <section class="abs recent">
    <h2 class="section-title">Recent Products</h2>
    <div class="dotted"></div>
    <div class="product-grid">
      <div class="product"><div class="product-name">Product Name</div><div class="product-img img-a" role="img" aria-label="Wooden cot with dresser"></div><div class="price">$ 00.00</div><div class="product-actions"><span>Add to Cart</span><span>View more</span></div></div>
      <div class="product"><div class="product-name">Product Name</div><div class="product-img img-b" role="img" aria-label="White daybed in a bright room"></div><div class="price">$ 00.00</div><div class="product-actions"><span>Add to Cart</span><span>View more</span></div></div>
      <div class="product"><div class="product-name">Product Name</div><div class="product-img img-c" role="img" aria-label="Dark wood cot"></div><div class="price">$ 00.00</div><div class="product-actions"><span>Add to Cart</span><span>View more</span></div></div>
      <div class="product"><div class="product-name">Product Name</div><div class="product-img img-d" role="img" aria-label="Dark wood wardrobe and cot set"></div><div class="price">$ 00.00</div><div class="product-actions"><span>Add to Cart</span><span>View more</span></div></div>
      <div class="product"><div class="product-name">Product Name</div><div class="product-img img-a" role="img" aria-label="Wooden cot with dresser"></div><div class="price">$ 00.00</div><div class="product-actions"><span>Add to Cart</span><span>View more</span></div></div>
      <div class="product"><div class="product-name">Product Name</div><div class="product-img img-b" role="img" aria-label="White daybed in a bright room"></div><div class="price">$ 00.00</div><div class="product-actions"><span>Add to Cart</span><span>View more</span></div></div>
      <div class="product"><div class="product-name">Product Name</div><div class="product-img img-c" role="img" aria-label="Dark wood cot"></div><div class="price">$ 00.00</div><div class="product-actions"><span>Add to Cart</span><span>View more</span></div></div>
      <div class="product"><div class="product-name">Product Name</div><div class="product-img img-d" role="img" aria-label="Dark wood wardrobe and cot set"></div><div class="price">$ 00.00</div><div class="product-actions"><span>Add to Cart</span><span>View more</span></div></div>
    </div>
  </section>

  <aside class="abs newsletter">
    <h3>Subscribe for News Letter</h3>
    <div class="dotted"></div>
    <div class="email">Enter your mail ID</div>
    <div class="submit">SUBMIT</div>
  </aside>

  <aside class="abs promo">
    <div class="promo-img" role="img" aria-label="Modern white cot with walnut frame"></div>
    <div class="promo-badge" role="img" aria-label="Satisfaction guarantee badge"></div>
    <h3>Quis autem veleum</h3>
    <p>Sed ut perspiciatis unde omnis iste natus error sit voluptatem accusantium dolor emque laudantium.</p>
    <div class="promo-cart">
      <svg width="14" height="12" viewBox="0 0 14 12"><path d="M0 1h2.5l2 7h7l1.5-5H4" fill="none" stroke="#fff" stroke-width="1.4"/><circle cx="5.5" cy="10.5" r="1.2" fill="#fff"/><circle cx="10.5" cy="10.5" r="1.2" fill="#fff"/></svg>
      Add to Cart</div>
    <div class="promo-more">View more
      <svg width="11" height="9" viewBox="0 0 11 9"><path d="M0 4.5h9M6 1l3.5 3.5L6 8" fill="none" stroke="#fff" stroke-width="1.6"/></svg>
    </div>
  </aside>

  <div class="abs rule" style="top:967px"></div>
  <h2 class="abs section-title testimonials-title">What Our Client’s Says About Us</h2>
  <section class="abs testimonial">
    <span class="quote-mark" style="left:12px;top:8px">“</span>
    <p>At vero eos et accusamus et iusto odio dignissimos ducimus qui blanditiis praesentium voluptatum deleniti atque corrupti quos dolores et quas molestias excepturi sint occaecati cupiditate non provident, similique.</p>
    <cite>Client Name, City</cite>
    <span class="quote-mark" style="right:14px;top:50px">”</span>
  </section>

  <footer class="abs site-footer">
    <nav class="footer-links"><span>Home</span><span>About us</span><span>Our Products</span><span>Shipping Details</span><span>Client’s Testimonials</span><span>Special Offers</span><span>Contact Us</span><span>My Cart</span><span>My Account</span><span>Check out</span><span>Login</span><span>Register</span><span>Help</span></nav>
    <div class="copyright">Copyright © 2012 www.littlenestshop.com &nbsp;All rights reserved.</div>
    <div class="social"><i></i><i></i></div>
  </footer>
</div>
</body>
</html>
```